Anzeigengestaltung für Gas- und Wasserinstallationsunternehmen
Zielgruppe
Gas- und Wasserinstallation, wir bauen, warten und sanieren Bäder und Heizungsanlagen
Wir wollen Leute im Alter 26-45 Jahre ansprechen, mit Berufserfahrung
Aufgabenstellung
Dass wir einen Kundendienstmonteur für Öl- und Gasfeuerung suchen

```html
<!DOCTYPE html>
<html lang="de">
<head>
<meta charset="utf-8">
<title>Stellenanzeige Kundendienstmonteur – Thermora GmbH</title>
<link rel="stylesheet" href="https://fonts.googleapis.com/css2?family=Fira+Sans:wght@400;500;600&display=swap">
<style>
  :root {
    --ember-dark: #1e0d07;
    --ember-mid: #4a1d0a;
    --flame: #e8862a;
    --flame-light: #ffcf7a;
    --panel: rgba(12, 22, 16, 0.88);
    --band-green: #12a55a;
    --band-blue: #1670c2;
    --white: #ffffff;
  }
  * { margin: 0; padding: 0; box-sizing: border-box; }
  html, body { width: 1200px; height: 830px; overflow: hidden; background: #ffffff; }
  body { font-family: "Fira Sans", Arial, sans-serif; color: var(--white); }

  .ad { position: relative; width: 1200px; height: 830px; overflow: hidden; }

  .hero-photo {
    position: absolute; left: 0; top: 0; width: 1200px; height: 619px;
    background:
      radial-gradient(ellipse 300px 380px at 280px 330px, rgba(255, 190, 100, 0.85), rgba(232, 120, 40, 0.55) 45%, rgba(0,0,0,0) 75%),
      radial-gradient(ellipse 420px 260px at 900px 560px, rgba(200, 90, 30, 0.45), rgba(0,0,0,0) 70%),
      linear-gradient(120deg, var(--ember-mid) 0%, var(--ember-dark) 45%, #3b1608 100%);
  }

  .headline {
    position: absolute; left: 495px; top: 38px;
    font-weight: 600; font-size: 50px; line-height: 66px;
  }
  .headline .line-two { display: block; padding-left: 77px; }

  .tagline {
    position: absolute; right: 76px; top: 178px; text-align: right;
    font-weight: 600; font-size: 30px; line-height: 46px;
  }

  .job-panel {
    position: absolute; left: 473px; top: 298px; width: 727px; height: 299px;
    background: var(--panel); padding: 16px 20px 0 22px;
  }
  .job-title { font-weight: 600; font-size: 24px; line-height: 32px; margin-bottom: 8px; }
  .requirements { list-style: none; font-size: 17px; line-height: 27.5px; }
  .requirements li { position: relative; padding-left: 20px; }
  .requirements li::before {
    content: ""; position: absolute; left: 2px; top: 12px;
    width: 6px; height: 6px; border-radius: 50%; background: var(--white);
  }

  .contact-band {
    position: absolute; left: 0; top: 619px; width: 1200px; height: 211px;
    background: linear-gradient(90deg, var(--band-green) 0%, #139a7a 50%, var(--band-blue) 100%);
  }
  .brand {
    position: absolute; left: 40px; top: 30px; display: flex; align-items: center; gap: 22px;
  }
  .brand-dot { width: 92px; height: 92px; border-radius: 50%; background: var(--white); opacity: 0.9; }
  .brand-name { font-weight: 600; font-size: 38px; letter-spacing: 0.5px; }

  .company-address { position: absolute; left: 44px; top: 114px; font-size: 20px; line-height: 27px; }
  .company-address strong { font-weight: 600; font-size: 19px; }

  .application-note { position: absolute; left: 624px; top: 40px; font-size: 20px; line-height: 27px; }

  .phone-lines { position: absolute; left: 516px; top: 143px; font-size: 20px; line-height: 27px; }
  .web-lines { position: absolute; left: 864px; top: 143px; font-size: 20px; line-height: 27px; }
</style>
</head>
<body>
<main class="ad">
  <div class="hero-photo" role="img" aria-label="Foto: Handwerker in Latzhose mit Hammer, umgeben von Flammen"></div>

  <h1 class="headline">Feuer und Flamme <span class="line-two">für Ihren Beruf?</span></h1>

  <p class="tagline">Wir auch!<br>Kommen Sie in unser Team.</p>

  <section class="job-panel">
    <h2 class="job-title">Wir suchen einen Kundendienstmonteur<br>für Öl- und Gasfeuerung (m/w/d):</h2>
    <ul class="requirements">
      <li>abgeschlossene Ausbildung als Gas-Installateur/in/ Monteur/in mit guten Kenntnissen der Ölheizungstechnik oder ausgebildeter Heizungsmonteur</li>
      <li>mehrjährige Berufserfahrung im vorgenannten Ausbildungsfeld</li>
      <li>lösungsorientierte, selbstständige und teamorientierte Arbeitsweise</li>
      <li>Führerschein Klasse B</li>
      <li>Bewusstsein für kreative und innovative Lösungen</li>
      <li>Zukunftsorientiertes Denken und Arbeiten</li>
    </ul>
  </section>

  <footer class="contact-band">
    <div class="brand">
      <span class="brand-dot"></span>
      <span class="brand-name">THERMORA GMBH</span>
    </div>

    <p class="company-address">
      <strong>Thermora GmbH</strong><br>
      Gesellschaft für Versorgungsanlagen mbH<br>
      Lindenweg 14 | 10115 Berlin
    </p>

    <p class="application-note">
      Schicken Sie uns Ihre aussagekräftigen Unterlagen<br>
      (Anschreiben, Lebenslauf mit Lichtbild, Zeugnissen)<br>
      bitte schriftlich an:
    </p>

    <p class="phone-lines">
      Tel. : +49 (0)30 12 34 - 5600<br>
      Fax : +49 (0)30 12 34 - 5601
    </p>

    <p class="web-lines">
      info@thermora-gmbh.de<br>
      www.thermora-gmbh.de
    </p>
  </footer>
</main>
</body>
</html>
```